Exciting Wordpress Project: New Consulting Firm

A wordpress design is needed for my new consulting company, Verbrook Partners.

The site should have a modern feel to it and use the colour scheme from the attached 3 vector files.

I only know a little about Wordpress but the site should be mobile friendly.

The following menu options should be created:
1. Home
2. Verbrook service lines (with sub-menus)
3. Our people
4. Verbrook case studies
5. The Verbrook story
6. Contact Verbrook
Updates

Reason: Allow just one or two more designs to come in before deciding.

Target Market(s)

Government departments and medium private sector organisations

Industry/Entity Type

It Company

Requirements
Must have
• 1. Inclue Verbrook logo at top of each page
2. Slider on the home page
3. Global navigation
4. Drop down navigation
5. Social media links
6. Search and contact details at the top of the home page
7. Home page to fit on one screen
8. Terms & Conditions, Privacy Policy at the bottom of the home page
9. Newsletter (i.e. postwren) subscription on home page
Nice to have
• 1. Background watermark from the Verbrook logo
2. A layout similar to the photo attached - however open to different ideas

```html
<!DOCTYPE html>
<html lang="en">
<head>
<meta charset="utf-8">
<title>Verbrook Partners</title>
<link rel="stylesheet" href="https://fonts.googleapis.com/css2?family=Open+Sans:wght@400;600&family=Oswald:wght@500&family=Arimo&display=swap">
<style>
  :root {
    --white: #ffffff;
    --ink: #6d6e71;
    --ink-dark: #4a4a4c;
    --nav-bg: #f2f2f2;
    --nav-active: #d6d6d6;
    --sky: #29a8e0;
    --sky-light: #4fb8e7;
    --sun: #f6e934;
    --sun-fold: #f2a516;
    --arrow: #f8dc14;
    --footer-bg: #e6e7e9;
    --footer-ink: #58595b;
    --social: #9c9d9f;
    --accent: #29a8e0;
  }
  * { box-sizing: border-box; margin: 0; padding: 0; }
  html, body { width: 1200px; height: 854px; overflow: hidden; background: var(--white); }
  body { font-family: "Open Sans", sans-serif; color: var(--ink); }
  .page { position: relative; width: 1200px; height: 854px; overflow: hidden; }

  .brand { position: absolute; left: 515px; top: 24px; width: 200px; text-align: center;
    font-size: 22px; font-weight: 600; letter-spacing: 1px; color: var(--ink); }
  .call { position: absolute; left: 872px; top: 44px; font-size: 17.5px; color: var(--ink); }
  .call span { color: var(--accent); }

  .nav { position: absolute; left: 0; top: 77px; width: 1200px; height: 40px;
    background: var(--nav-bg); box-shadow: 0 1px 4px rgba(0,0,0,.25); }
  .nav a { position: absolute; top: 0; height: 40px; line-height: 40px; font-size: 11.5px;
    color: var(--ink); text-decoration: none; }
  .nav .is-active { background: var(--nav-active); left: 167px; width: 97px; text-align: center; }

  .hero { position: absolute; left: 167px; top: 117px; width: 867px; height: 221px;
    background: linear-gradient(160deg, #cfd1d3 0%, #f3f4f5 45%, #dcdddf 70%, #bfc1c4 100%); }
  .search { position: absolute; left: 815px; top: 126px; width: 208px; height: 28px;
    background: var(--white); border-radius: 14px; box-shadow: 0 1px 3px rgba(0,0,0,.35);
    font-size: 11px; line-height: 28px; padding-left: 14px; color: #9a9b9d; }
  .search svg { position: absolute; right: 6px; top: 4px; }

  .band { position: absolute; left: 0; top: 376px; width: 1200px; height: 218px; background: var(--sky); }
  .band-edge { position: absolute; left: 0; top: 592px; width: 1200px; height: 0;
    border-top: 2px dashed #c9dd3a; }

  .dome { position: absolute; left: 376px; top: 290px; width: 439px; height: 120px;
    background: var(--sky); border-radius: 50%; }
  .dome-title { position: absolute; left: 376px; top: 294px; width: 439px; text-align: center;
    font-size: 38px; color: var(--white); letter-spacing: -.5px; }

  .ribbon { position: absolute; left: 152px; top: 339px; width: 897px; height: 36px; background: var(--sun); }
  .fold { position: absolute; top: 375px; }

  .cards { position: absolute; left: 167px; top: 376px; width: 868px; height: 180px;
    background: var(--sky-light); border: 1px dashed rgba(255,255,255,.85); border-top: none;
    box-shadow: 0 2px 4px rgba(0,0,0,.15); }
  .divider { position: absolute; top: 376px; height: 180px; border-left: 1px dashed rgba(255,255,255,.85); }

  .service { position: absolute; top: 350px; width: 210px; margin-left: -105px; text-align: center; color: var(--white); }
  .service-badge { width: 82px; height: 82px; margin: 0 auto; border-radius: 50%; background: var(--white);
    display: flex; align-items: center; justify-content: center; }
  .service-title { margin-top: 15px; font-size: 19.5px; line-height: 24px; }
  .service-text { margin-top: 3px; font-size: 11.5px; line-height: 15px; }
  .service-go { position: absolute; top: 544px; margin-left: -11px; }

  .footer { position: absolute; left: 0; top: 653px; width: 1200px; height: 201px;
    background: var(--footer-bg); box-shadow: 0 -2px 4px rgba(0,0,0,.12); }
  .footer-col { position: absolute; top: 14px; font-family: "Arimo", sans-serif; }
  .footer-col h3 { font-family: "Oswald", sans-serif; font-weight: 500; font-size: 12.5px;
    color: var(--ink-dark); margin-bottom: 4px; }
  .footer-col li { list-style: none; font-size: 8.5px; line-height: 10.5px; color: var(--footer-ink); }
  .social { position: absolute; left: 890px; top: 22px; display: flex; gap: 5.5px; }
  .social span { width: 21.5px; height: 21.5px; border-radius: 4px; background: var(--social); }
  .copyright { position: absolute; left: 0; top: 139px; width: 1208px; text-align: center;
    font-family: "Arimo", sans-serif; font-size: 8.5px; color: #231f20; }
</style>
</head>
<body>
<div class="page">
  <svg width="0" height="0" style="position:absolute">
    <defs>
      <symbol id="network" viewBox="0 0 60 60">
        <g stroke="#29a8e0" stroke-width="3" fill="none">
          <circle cx="30" cy="30" r="7"/>
          <line x1="30" y1="23" x2="30" y2="8"/><line x1="30" y1="37" x2="30" y2="52"/>
          <line x1="24" y1="26" x2="11" y2="19"/><line x1="36" y1="26" x2="49" y2="19"/>
          <line x1="24" y1="34" x2="11" y2="41"/><line x1="36" y1="34" x2="49" y2="41"/>
        </g>
        <g fill="#29a8e0">
          <circle cx="30" cy="7" r="4.5"/><circle cx="30" cy="53" r="4.5"/>
          <circle cx="9" cy="18" r="4.5"/><circle cx="51" cy="18" r="4.5"/>
          <circle cx="9" cy="42" r="4.5"/><circle cx="51" cy="42" r="4.5"/>
        </g>
      </symbol>
      <symbol id="go" viewBox="0 0 22 22">
        <circle cx="11" cy="11" r="11" fill="#f8dc14"/>
        <path d="M9 6.5 L14.5 11 L9 15.5 Z" fill="#29a8e0"/>
      </symbol>
    </defs>
  </svg>

  <header>
    <div class="brand">Verbrook Partners</div>
    <div class="call"><span>CALL</span> 1800 42 17350</div>
  </header>

  <nav class="nav">
    <a class="is-active" href="#">HOME</a>
    <a href="#" style="left:297px">VERBROOK SERVICE LINES</a>
    <a href="#" style="left:455px">OUR PEOPLE</a>
    <a href="#" style="left:561px">VERBROOK CASE STUDIES</a>
    <a href="#" style="left:709px">THE VERBROOK STORY</a>
    <a href="#" style="left:868px">CONTACT VERBROOK</a>
  </nav>

  <div class="hero" role="img" aria-label="Slider photo: close-up of a white keyboard with a consultancy key"></div>
  <div class="search">SEARCH
    <svg width="20" height="20" viewBox="0 0 20 20"><circle cx="10" cy="10" r="8.5" fill="none" stroke="#29a8e0" stroke-width="1.5"/><circle cx="10" cy="10" r="5.5" fill="#9c9d9f"/></svg>
  </div>

  <div class="band"></div>
  <div class="band-edge"></div>
  <div class="dome"></div>
  <div class="dome-title">WHAT WE DO?</div>
  <div class="ribbon"></div>
  <svg class="fold" style="left:152px" width="15" height="10"><path d="M0 0 H15 V10 Z" fill="#f2a516"/></svg>
  <svg class="fold" style="left:1034px" width="15" height="10"><path d="M15 0 H0 V10 Z" fill="#f2a516"/></svg>

  <section class="cards"></section>
  <div class="divider" style="left:380px"></div>
  <div class="divider" style="left:607px"></div>
  <div class="divider" style="left:815px"></div>

  <article class="service" style="left:272px">
    <div class="service-badge"><svg width="50" height="50"><use href="#network"/></svg></div>
    <h2 class="service-title" style="font-weight:400">ABCD Solutions</h2>
    <p class="service-text">Lorem ipsum dolor sit amet,<br>consectetur adipisicing elit, sed<br>do eiusmod tempor incididunt</p>
  </article>
  <article class="service" style="left:494px">
    <div class="service-badge"><svg width="50" height="50"><use href="#network"/></svg></div>
    <h2 class="service-title" style="font-weight:400">XYZ Solutions</h2>
    <p class="service-text">Lorem ipsum dolor sit amet,<br>consectetur adipisicing elit, sed<br>do eiusmod tempor incididunt</p>
  </article>
  <article class="service" style="left:713px">
    <div class="service-badge"><svg width="50" height="50"><use href="#network"/></svg></div>
    <h2 class="service-title" style="font-weight:400">ABCD Solutions</h2>
    <p class="service-text">Lorem ipsum dolor sit amet,<br>consectetur adipisicing elit, sed<br>do eiusmod tempor incididunt</p>
  </article>
  <article class="service" style="left:921px">
    <div class="service-badge"><svg width="50" height="50"><use href="#network"/></svg></div>
    <h2 class="service-title" style="font-weight:400">XYZ Solutions</h2>
    <p class="service-text">Lorem ipsum dolor sit amet,<br>consectetur adipisicing elit, sed<br>do eiusmod tempor incididunt</p>
  </article>
  <svg class="service-go" style="left:272px;top:543px" width="22" height="22"><use href="#go"/></svg>
  <svg class="service-go" style="left:494px" width="22" height="22"><use href="#go"/></svg>
  <svg class="service-go" style="left:713px" width="22" height="22"><use href="#go"/></svg>
  <svg class="service-go" style="left:921px" width="22" height="22"><use href="#go"/></svg>

  <footer class="footer">
    <div class="footer-col" style="left:182px">
      <h3>About</h3>
      <ul><li>Homepage</li><li>Verbrook Service Lines</li><li>Our People</li><li>Verbrook Case Studies</li><li>The Verbrook Story</li></ul>
    </div>
    <div class="footer-col" style="left:359px">
      <h3>Privacy &amp; Security</h3>
      <ul><li>Privacy Policy</li><li>Terms of Use</li></ul>
    </div>
    <div class="footer-col" style="left:558px">
      <h3>Contact</h3>
      <ul><li>Contact Verbrook</li><li>Careers</li><li>Follow us on Friendwall</li></ul>
    </div>
    <div class="social" aria-label="Social media links"><span></span><span></span><span></span><span></span></div>
    <p class="copyright">© 2013 &nbsp;Verbrook Partners- All rights reserved. Reproduction without permission is prohibited</p>
  </footer>
</div>
</body>
</html>
```